Brochure Design Project

A4 Portrait
8 Page Sales brochure for Automatic Coffee Machines for Offices.
We have 4 products in 4 cateries.
Small Office
Medium Office
Large Office
Whole Company / Food Service.

There will be a product image plus 3-4 accessories for each product

Then a brief sales pitch text for each product.

We supply to public listed companies therefore it has to be professional, well presented and eye catching.

Thank you
Updates

I will make the budget $200

Project Deadline Extended

Hello,

Please note that I've made changes to the job brief. 

Thanks

Walter 

Hi 

Please find attached contents in pdf for your implementation.

1. Small Office Solution
2. Medium Office Solution 
3. Large Office Solution
4. Whole Company Solution
5. Food Service

Thanks 

Walter

Project Deadline Extended

Hi All

Budget increased to $200, extended project by 7 more days.

Thank you

Howard Benlo

Target Market(s)

Big Corporate Companies in major Australian cities

Industry/Entity Type

It Company

Requirements
Must have
• A4 Portrait
8 Page photo and sales pitch text. One product per page starting from 3nd page
5 products into 5 categories of

Page 2 will tell about our company and services

Small Office Solution (page 3)
$16 per day)

Medium Office Solution (page 4)
$18 per day)

Large Office Solution (page 5)
$19 per day)

Whole Company (page 6)
$24 per day)

Food Service Solution (page 7
$28 per day

Each product page will highlight
eg
Small Office Solution
$16 per day)

Each page will have 3-4 accessories (photos)

Page 8 Our logo, address & Conatct details - Please see for contact details http://www.brewvanta.com.au/brew_va
Nice to have
• Logo, photo of coffee machine, an office environment where people are kind of enjoying coffee in a lounge.

Should not have
• Not messy, no old style,

```html
<!DOCTYPE html>
<html lang="en">
<head>
<meta charset="utf-8">
<title>Office Coffee Solutions</title>
<link href="https://fonts.googleapis.com/css2?family=EB+Garamond:wght@400;500&family=Arimo:wght@400;700&display=swap" rel="stylesheet">
<style>
:root{
  --brown:#5b3526;
  --brown-dark:#4a2a1e;
  --tan:#d6a97c;
  --tan-title:#dcaa7e;
  --text:#333;
  --muted:#555;
  --accent:#e07b2c;
  --paper:#ffffff;
  --fade:#e9e9e9;
}
*{margin:0;padding:0;box-sizing:border-box}
html,body{width:1200px;height:854px;overflow:hidden;background:var(--paper)}
body{font-family:"Arimo",Arial,sans-serif;color:var(--text);position:relative}
.spread{position:relative;width:1200px;height:854px;background:linear-gradient(to bottom,#fff 0,#fff 620px,var(--fade) 828px)}
.page{position:absolute;top:0;width:600px;height:854px}
.page--left{left:0}
.page--right{left:600px;border-left:1px solid #d8c7b8}
.header{position:absolute;left:0;top:0;width:600px;height:188px;background:var(--brown)}
.stripe{position:absolute;left:0;top:188px;width:600px;height:10px;background:var(--tan)}
.footer{position:absolute;left:0;top:828px;width:600px;height:26px;background:var(--brown)}
.title{position:absolute;left:40px;top:72px;font-family:"EB Garamond",Georgia,serif;font-weight:400;font-size:38px;color:var(--tan-title);white-space:nowrap}
.subtitle{position:absolute;left:40px;top:116px;font-family:"EB Garamond",Georgia,serif;font-size:20px;line-height:25px;color:#fff}
.corner{position:absolute;left:420px;top:47px;width:30px;height:30px;background:#fff}
.price{position:absolute;left:450px;top:77px;width:150px;height:90px;background:var(--tan);color:var(--brown-dark);font-family:"EB Garamond",Georgia,serif;text-align:center}
.price__amount{position:absolute;left:0;right:0;top:4px;font-size:56px;line-height:60px}
.price__amount small{font-size:20px;vertical-align:12px;margin-right:2px}
.price__unit{position:absolute;left:0;right:0;top:62px;font-size:20px;letter-spacing:.5px}
.dimension{position:absolute;left:45px;top:235px;font-size:9px;font-weight:700;color:#444}
.dimension span{display:block;font-size:11px;font-weight:400;margin-top:2px}
.specs{position:absolute;left:55px;list-style:none;font-size:9.5px;color:var(--muted)}
.specs li{margin-bottom:6px;line-height:11px}
.specs--bullet li{padding-left:10px;position:relative}
.specs--bullet li::before{content:"";position:absolute;left:0;top:3px;width:5px;height:5px;background:#888}
.specs .highlight{color:var(--accent);font-weight:700;font-size:10px}
.specs h3{font-size:10.5px;font-weight:700;color:#333;margin:14px 0 8px}
.features{position:absolute;width:270px}
.features h2{font-size:12px;font-weight:700;color:#111;padding-left:10px;position:relative;margin-bottom:10px}
.features h2::before,.feature h4::before{content:"";position:absolute;left:0;top:3px;width:6px;height:6px;background:#111}
.feature{margin-bottom:12px}
.feature h4{font-size:9px;font-weight:700;color:#111;padding-left:10px;position:relative;margin-bottom:4px}
.feature p{font-size:8.6px;line-height:11.5px;color:#333;padding-left:10px;text-align:justify}
.product{position:absolute;border-radius:4px}
</style>
</head>
<body>
<div class="spread">

  <section class="page page--left">
    <div class="header"></div>
    <div class="stripe"></div>
    <h1 class="title">Medium Office Solution</h1>
    <p class="subtitle">Coffee and Hot Chocolate in Perfect Sync<br>where quality and reliability are key</p>
    <div class="corner"></div>
    <div class="price"><div class="price__amount"><small>$</small>18</div><div class="price__unit">PER DAY</div></div>

    <p class="dimension">Dimension: (coffee machine)<span>W: 430 D: 500 H: 695</span></p>
    <ul class="specs" style="top:275px">
      <li>Fresh Coffee</li>
      <li style="margin-top:11px">Fresh Milk</li>
      <li>Automatic Cleaning Program<br>no parts removed.<br>no manuals required</li>
      <li>30 Drinks of your choice</li>
      <li>Easy Operation</li>
      <li>Fast and Quiet</li>
      <li>Robust Body &amp; Metal Brewer</li>
      <li>HACCP Certified</li>
      <li><h3 style="margin-top:20px">Cafe quality drinks</h3></li>
      <li>Up to 30 selections including:</li>
      <li>Cappuccino</li>
      <li>Hot Chocolate</li>
      <li>Espresso</li>
      <li>Latte</li>
      <li>Mocha</li>
      <li>Chai Latte</li>
      <li>Strength and cup size options</li>
    </ul>

    <div class="features" style="left:292px;top:250px">
      <h2>Features</h2>
      <div class="feature"><h4>Fresh Coffee - Micro Fine Sieve</h4><p>The Micro-Fine Sieve is a key guarantee for optimal coffee. Over 45,150 conical holes across an area of 1075 mm2. This ensures dreg-free and high quality coffee with optimum extraction.</p></div>
      <div class="feature"><h4>Fully Automatic Milk Cleaning Program- HACCP Certified</h4><p>Milk &amp; Coffee systems are cleaned Automatically. There's no removal of parts and components. The only company that is HACCP tested and certified</p></div>
      <div class="feature"><h4>Easy Operation - Graphic Display:</h4><p>30 Drink selections of your choice, never before has real coffee preparation been so simple and fast to prepare with the flair of a trained Barista.</p></div>
      <div class="feature"><h4>Hot Chocolate and Chai Latte Maker</h4><p>Integrated Chocolate and Chai Latte module provides you with the option to dispense different Coffee, Chocolate and Chai specialities with milk. There's something for everyone.</p></div>
      <div class="feature"><h4>Choices</h4><p>Strength of drinks can be programed in 3 levels of Mild, Medium and Strong. Easy access to Small, Medium and Large cups are also available on the one screen</p></div>
    </div>

    <div class="product" role="img" aria-label="Photo of the medium office automatic coffee machine with bean hoppers and display" style="left:155px;top:622px;width:96px;height:188px;background:linear-gradient(to bottom,#8a8a8a,#2a2a2a 40%,#1a1a1a)"></div>
    <div class="product" role="img" aria-label="Photo of a cup warmer cabinet with white cups" style="left:330px;top:625px;width:106px;height:185px;background:linear-gradient(to bottom,#f2f2f2,#b8b4ae)"></div>
    <div class="footer"></div>
  </section>

  <section class="page page--right">
    <div class="header"></div>
    <div class="stripe"></div>
    <h1 class="title">Large Office Solution</h1>
    <p class="subtitle">The Corporate Office Partner in<br>Automatic Coffee Making.</p>
    <div class="corner"></div>
    <div class="price"><div class="price__amount"><small>$</small>19</div><div class="price__unit">PER DAY</div></div>

    <p class="dimension" style="left:53px;top:229px">Dimension: (coffee machine)<span>W: 325 D: 560 H: 818</span></p>
    <ul class="specs specs--bullet" style="left:52px;top:266px">
      <li>Fresh Coffee</li>
      <li>Fresh Milk</li>
      <li>Automatic Cleaning Program<br>no parts removed.<br>no manuals required</li>
      <li>24 Drinks of your choice</li>
      <li>Easy Operation</li>
      <li>Fast and Quiet</li>
      <li>Robust Metal Brewer</li>
      <li class="highlight">Cafe quality drinks</li>
      <li>Up to 24 selections including:</li>
      <li>Cappuccino</li>
      <li>Espresso</li>
      <li>Latte</li>
      <li>Strength and cup size options</li>
    </ul>

    <div class="features" style="left:48px;top:508px;width:210px">
      <h2>Features</h2>
      <div class="feature"><h4>Choices</h4><p style="text-align:left">Strength of drinks can be programed in 3 levels of Mild, Medium and Strong. Easy access to Small, Medium and Large cups are also available on the one screen</p></div>
    </div>

    <div class="features" style="left:276px;top:262px;width:280px">
      <div class="feature"><h4>Fresh Coffee</h4><p>At the push of a button, the machine grinds, tamps, brews and pours your favorite coffee in the shortest possible time, yet with the flair and punch of a trained barista.</p></div>
      <div class="feature"><h4>Fresh Milk - MFT Milk Flow Technology:</h4><p>Milk pump to dispense milk-based drinks at the desired temperature and texture consistently.</p></div>
      <div class="feature"><h4>Fully Automated Milk Cleaning Program- PureCycle</h4><p>Milk &amp; Coffee systems are cleaned Automatically. There's no removal of parts and components. The PureCycle ensures the milk circuit, coffee and steam boiler are hygienically cleaned.</p></div>
      <div class="feature"><h4>Easy Operation - Graphic Display:</h4><p>24 drink selections of your choice, drink selection icons, trademarks and commercial can be easily customized. There is no need for manuals as all operating instructions are communicated via the large LCD.</p></div>
      <div class="feature"><h4>Chocolate Module (Optional)</h4><p>A Matching Slim Line Chocolate module can be added to dispense Hot Chocolate, Mocha and any other chocolate specialties with milk. There's something for everyone.</p></div>
      <div class="feature"><h4>Consistency - ChillGuard:</h4><p>Detects over temperature of milk and stop milk-based drinks. Milk sensor to detect empty milk carton &amp; stop milk-based drinks to ensure consistency and minimize wastage.</p></div>
    </div>

    <div class="product" role="img" aria-label="Photo of a cup warmer cabinet with white cups" style="left:128px;top:636px;width:80px;height:176px;background:linear-gradient(to bottom,#f0f0f0,#c4c6c8)"></div>
    <div class="product" role="img" aria-label="Photo of a slim chocolate module" style="left:268px;top:634px;width:62px;height:180px;background:linear-gradient(to bottom,#d9dde0,#3a3d40 40%,#2a2c2e)"></div>
    <div class="product" role="img" aria-label="Photo of a milk fridge unit with open door" style="left:378px;top:636px;width:82px;height:176px;background:linear-gradient(to bottom,#e6e8ea,#9ea2a6)"></div>
    <div class="footer"></div>
  </section>

</div>
</body>
</html>
```